Blockchain Analytics Firm Needs Logo And Website Design

We need a logo and a very basic website for a company based in Haldstad, Sweden called 'Vextor'. We build custom machine learning and AI solutions for companies based on blockchain. We are not picky about the colors, but the design should communicate modernity and stability.
We like the following websites:
https://www.hollowpine.co.uk/
https://www.tavromeridian.com/
Target Market(s)
Our customers are startups that have their own product based on blockchain or other distributed ledger technology.
Industry/Entity Type
It Company
Contact Information for Business Card
Name, title and email address
Logo Text
Our company name and "Blockchain Analytics"
Colors
Designer to choose colors to be used in the design.
Requirements
Must have
- The website and logo need to be modern and clean. In the beginning, we will not be filling out all sections of the website (team, clients, etc.) but we will need to have these set up so we can eventually use them.
Nice to have
- We like angular graphics and some animations on the webpage would be nice.

```html
<!DOCTYPE html>
<html lang="en">
<head>
<meta charset="utf-8">
<title>Vextor – Blockchain Analytics</title>
<link href="https://fonts.googleapis.com/css2?family=Lato:wght@400;700;900&display=swap" rel="stylesheet">
<style>
  :root {
    --ink: #222222;
    --night: #1c1c1e;
    --black: #111111;
    --red: #e8414a;
    --blue: #1a7fc9;
    --navy: #0e5d9c;
    --blush: #fcefeb;
    --white: #ffffff;
    --grey: #8a8a8a;
    --text: #444444;
  }
  * { box-sizing: border-box; margin: 0; padding: 0; }
  html, body { width: 1200px; height: 3383px; overflow: hidden; background: var(--white); }
  body { font-family: "Lato", sans-serif; color: var(--text); }
  .page { position: relative; width: 1200px; height: 3383px; overflow: hidden; }
  .abs { position: absolute; }

  /* header */
  .site-header { left: 0; top: 0; width: 1200px; height: 131px; background: var(--ink); }
  .brand-dot { left: 70px; top: 34px; width: 56px; height: 56px; border-radius: 50%; background: var(--red); }
  .brand-name { left: 142px; top: 28px; font-size: 36px; font-weight: 700; color: var(--red); letter-spacing: 2px; line-height: 1; }
  .brand-tag { left: 142px; top: 70px; font-size: 23px; color: var(--blue); line-height: 1; }
  .nav-icons { left: 1052px; top: 54px; }

  /* background shapes */
  .shapes { left: 0; top: 0; width: 1200px; height: 3383px; }

  /* hero */
  .hero-title { left: 165px; top: 282px; font-size: 44px; font-weight: 700; color: var(--red); letter-spacing: 2px; line-height: 1.05; }
  .hero-sub { left: 165px; top: 332px; font-size: 32px; color: var(--blue); line-height: 1.1; }
  .hero-text { left: 165px; top: 378px; width: 370px; font-size: 18.5px; line-height: 26px; color: var(--ink); }
  .btn { left: 165px; top: 456px; width: 151px; height: 42px; background: var(--blue); color: var(--white); font-size: 12px; font-weight: 700; letter-spacing: 1px; text-align: center; line-height: 42px; }
  .hero-video { left: 562px; top: 223px; width: 561px; height: 341px; border: 6px solid var(--white); box-shadow: 0 2px 10px rgba(0,0,0,.45); background: linear-gradient(100deg, #0b0b0d 0%, #1b1420 40%, #3a2440 70%, #1d1624 100%); }

  /* about */
  .about-title { left: 512px; top: 926px; font-size: 31px; line-height: 38px; color: var(--white); }
  .about-text { left: 512px; top: 1024px; width: 610px; font-size: 14.5px; line-height: 28px; color: #e6e6e6; }

  /* machine learning */
  .ml-title { left: 74px; top: 1342px; font-size: 33px; color: var(--white); }
  .ml-text { left: 74px; top: 1398px; width: 585px; font-size: 14.5px; line-height: 28px; font-weight: 700; color: var(--white); }
  .ml-figure { left: 767px; top: 1265px; width: 293px; height: 290px; border-radius: 40% 50% 30% 30%; background: radial-gradient(circle at 55% 45%, rgba(26,127,201,.35), rgba(26,127,201,.08) 70%, transparent 72%); }

  /* ai */
  .ai-title { right: 74px; top: 1857px; font-size: 33px; color: var(--white); text-align: right; }
  .ai-text { right: 74px; top: 1913px; width: 570px; font-size: 14.5px; line-height: 28px; font-weight: 700; color: var(--white); text-align: right; }
  .ai-figure { left: 118px; top: 1795px; width: 282px; height: 313px; border-radius: 24px; background: radial-gradient(circle at 50% 45%, rgba(232,65,74,.28), rgba(232,65,74,.08) 65%, transparent 70%); }

  /* testimonial */
  .quote-band { left: 0; top: 2215px; width: 1200px; height: 334px; background: radial-gradient(ellipse at 40% 70%, #1a3a4e 0%, #0d1c28 45%, #070d14 100%); }
  .avatar { left: 548px; top: 2282px; width: 100px; height: 100px; border-radius: 50%; border: 4px solid #d8d8d8; background: linear-gradient(160deg, #9aa2ab, #4b525a); }
  .quote { left: 145px; top: 2397px; width: 910px; text-align: center; font-size: 15px; line-height: 30px; color: #e3e3e3; }
  .quote-name { left: 0; top: 2472px; width: 1200px; text-align: center; font-size: 16px; color: var(--blue); }

  /* blog */
  .blog-title { left: 74px; top: 2594px; font-size: 33px; color: #3a3a3a; }
  .blog-arrows { left: 1074px; top: 2606px; }
  .card { width: 512px; }
  .card-media { width: 512px; height: 212px; }
  .card-media.one { background: radial-gradient(circle at 52% 50%, #e0b24a 0%, #2d4a5c 30%, #0d1a24 75%); }
  .card-media.two { background: linear-gradient(120deg, #0b2236 0%, #24587c 45%, #4a8ab2 70%, #1d3c56 100%); }
  .card-body { padding: 0 14px; }
  .card-title { margin-top: 22px; font-size: 21px; font-weight: 700; color: var(--blue); }
  .card-text { margin-top: 8px; font-size: 14.5px; line-height: 26px; color: var(--text); }
  .card-meta { margin-top: 16px; display: flex; justify-content: space-between; font-size: 13.5px; color: var(--red); }
  .card-meta span { display: flex; align-items: center; gap: 8px; }

  /* footer */
  .site-footer { left: 0; top: 3140px; width: 1200px; height: 243px; background: var(--black); }
  .foot-dot { left: 74px; top: 3190px; width: 44px; height: 44px; border-radius: 50%; background: var(--red); }
  .foot-name { left: 132px; top: 3188px; font-size: 27px; font-weight: 700; color: var(--red); letter-spacing: 1px; }
  .foot-tag { left: 132px; top: 3220px; font-size: 17px; color: var(--blue); }
  .copyright { left: 74px; top: 3253px; font-size: 12px; line-height: 20px; color: #5a5a5a; }
  .social { left: 74px; top: 3310px; display: flex; gap: 20px; }
  .social i { display: block; width: 22px; height: 22px; border-radius: 50%; background: #5a5a5a; }
  .foot-head { font-size: 17px; font-weight: 700; color: var(--white); }
  .foot-line { font-size: 13px; line-height: 24px; color: #b5b5b5; }
  .col-address { left: 356px; top: 3172px; }
  .col-hours { left: 622px; top: 3172px; }
  .col-email { left: 898px; top: 3172px; }
  .hours-row { display: flex; gap: 24px; }
  .signup { margin-top: 20px; display: flex; }
  .signup-field { width: 190px; height: 37px; background: var(--white); font-size: 12px; color: #999; line-height: 37px; padding-left: 10px; }
  .signup-btn { width: 37px; height: 37px; background: var(--blue); display: flex; align-items: center; justify-content: center; }
</style>
</head>
<body>
<div class="page">

  <svg class="abs shapes" viewBox="0 0 532 1500" preserveAspectRatio="none" aria-hidden="true">
    <rect x="0" y="752" width="532" height="230" fill="#fcefeb"/>
    <path d="M0,170 L212,352 Q232,372 252,352 L470,105 Q490,80 462,58" fill="none" stroke="#8a8a8a" stroke-width="0.6"/>
    <path d="M160,560 L330,748" fill="none" stroke="#8a8a8a" stroke-width="0.5"/>
    <polygon points="-20,218 22,215 190,372 190,398 70,528 -20,528" fill="#0e5d9c" stroke="#0e5d9c" stroke-width="26" stroke-linejoin="round"/>
    <polygon points="338,292 532,415 532,560 338,742 134,540 134,492" fill="#1c1c1e" stroke="#1c1c1e" stroke-width="26" stroke-linejoin="round"/>
    <polygon points="-20,548 236,548 312,622 312,650 226,740 -20,740" fill="#e8414a" stroke="#e8414a" stroke-width="24" stroke-linejoin="round"/>
    <polygon points="545,770 316,770 222,860 302,962 545,962" fill="#1a7fc9" stroke="#1a7fc9" stroke-width="26" stroke-linejoin="round"/>
    <path d="M150,982 L232,935 M190,982 L250,948" fill="none" stroke="#e8414a" stroke-width="0.6"/>
  </svg>

  <header class="abs site-header"></header>
  <div class="abs brand-dot"></div>
  <div class="abs brand-name">VEXTOR</div>
  <div class="abs brand-tag">Blockchain Analytics</div>
  <svg class="abs nav-icons" width="80" height="30" viewBox="0 0 80 30" aria-label="Search and menu">
    <circle cx="15" cy="13" r="8" fill="none" stroke="#fff" stroke-width="3.5"/>
    <line x1="21" y1="19" x2="27" y2="25" stroke="#fff" stroke-width="4" stroke-linecap="round"/>
    <rect x="52" y="6" width="20" height="3.5" fill="#fff"/>
    <rect x="52" y="13.5" width="20" height="3.5" fill="#fff"/>
    <rect x="52" y="21" width="20" height="3.5" fill="#fff"/>
  </svg>

  <h1 class="abs hero-title">VEXTOR</h1>
  <div class="abs hero-sub">Blockchain Analytics</div>
  <p class="abs hero-text">Vivamus lobortis aliquam nulla venenatis porta venenatis tellus malesuada.</p>
  <div class="abs btn">LEARN MORE</div>
  <div class="abs hero-video" role="img" aria-label="Video still of two speakers presenting on stage in front of a projected company slide"></div>

  <h2 class="abs about-title">About<br>Vextor Data Analytic</h2>
  <p class="abs about-text">Vextor is a data analytics startup that can quickly deploy custom machine learning and AI solutions for companies based on Distributed Ledger Technologies (DLT) such as Blockchains.&nbsp; A massive amount of data is generated from these Smart Contracts, particularly from Internet of Things (IoT) applications.&nbsp; We combine this information with traditional data pipelines and present a complete package to our customer.</p>

  <h2 class="abs ml-title">Machine Learning</h2>
  <p class="abs ml-text">Curabitur tempor risus nec ipsum egestas, pellentesque dapibus est bibendum. Nullam condimentum bibendum nisl, at venenatis tellus malesuada a. Aliquam laoreet orci ligula, in sagittis magna vehicula eu. Integer at nisi at libero posuere viverra quis non turpis.</p>
  <div class="abs ml-figure" role="img" aria-label="Blue line illustration of a head profile with circuit nodes and a gear"></div>

  <div class="abs ai-figure" role="img" aria-label="Red line illustration of a brain inside a microchip"></div>
  <h2 class="abs ai-title">AI Solutions</h2>
  <p class="abs ai-text">Curabitur tempor risus nec ipsum egestas, pellentesque dapibus est bibendum. Nullam condimentum bibendum nisl, at venenatis tellus malesuada a. Aliquam laoreet orci ligula, in sagittis magna vehicula eu. Integer at nisi at libero posuere viverra quis non turpis.</p>

  <section class="abs quote-band" role="img" aria-label="Dark blue background of a glowing network over a city at night"></section>
  <div class="abs avatar" role="img" aria-label="Portrait of the person quoted"></div>
  <p class="abs quote">" Curabitur tempor risus nec ipsum egestas, pellentesque dapibus est bibendum.&nbsp; condimentum bibendum nisl, at venenatis tellus malesuada a. Aliquam laoreet orci ligula, in sagittis magna vehicula eu. Integer at nisi at libero posuere..."</p>
  <div class="abs quote-name">Name Heading</div>

  <h2 class="abs blog-title">Latest from the blog</h2>
  <svg class="abs blog-arrows" width="56" height="24" viewBox="0 0 56 24" aria-label="Previous and next">
    <path d="M14 4 L6 12 L14 20 M6 12 H22" fill="none" stroke="#bdbdbd" stroke-width="3"/>
    <path d="M42 4 L50 12 L42 20 M50 12 H34" fill="none" stroke="#1a7fc9" stroke-width="3"/>
  </svg>

  <article class="abs card" style="left:74px; top:2680px;">
    <div class="card-media one" role="img" aria-label="Glowing coin surrounded by finance icons on a dark circuit background"></div>
    <div class="card-body">
      <h3 class="card-title">Curabitur tempor risus nec ipsum egestas</h3>
      <p class="card-text">Pellentesque dapibus est bibendum&nbsp; condimentum bibendum nisl, at venenatis tellus malesuada a. Aliquam laoreet orci ligula, in sagittis magna vehicula eu. Integer at nisi at libero posuere...</p>
      <div class="card-meta"><span>Continue Reading</span><span><svg width="14" height="13" viewBox="0 0 14 13"><path d="M7 1C3.5 1 1 3.1 1 5.7c0 1.5.8 2.8 2.1 3.7L2.5 12l3-1.8c.5.1 1 .2 1.5.2 3.5 0 6-2.1 6-4.7S10.5 1 7 1z" fill="#e8414a"/></svg>7 Comments</span></div>
    </div>
  </article>

  <article class="abs card" style="left:613px; top:2680px;">
    <div class="card-media two" role="img" aria-label="Person touching a glowing blockchain interface on a screen"></div>
    <div class="card-body">
      <h3 class="card-title">Curabitur tempor risus nec ipsum egestas</h3>
      <p class="card-text">Pellentesque dapibus est bibendum&nbsp; condimentum bibendum nisl, at venenatis tellus malesuada a. Aliquam laoreet orci ligula, in sagittis magna vehicula eu. Integer at nisi at libero posuere...</p>
      <div class="card-meta"><span>Continue Reading</span><span><svg width="14" height="13" viewBox="0 0 14 13"><path d="M7 1C3.5 1 1 3.1 1 5.7c0 1.5.8 2.8 2.1 3.7L2.5 12l3-1.8c.5.1 1 .2 1.5.2 3.5 0 6-2.1 6-4.7S10.5 1 7 1z" fill="#e8414a"/></svg>7 Comments</span></div>
    </div>
  </article>

  <footer class="abs site-footer"></footer>
  <div class="abs foot-dot"></div>
  <div class="abs foot-name">VEXTOR</div>
  <div class="abs foot-tag">Blockchain Analytics</div>
  <p class="abs copyright">Copyright 2018 Company Name.<br>All Rights Reserved.</p>
  <div class="abs social" aria-label="Social links"><i></i><i></i><i></i><i></i><i></i></div>

  <div class="abs col-address">
    <div class="foot-head">Address Info</div>
    <p class="foot-line" style="margin-top:14px;">Norrvik Science Park,<br>Ekgatan 12, SE-712 44<br>Haldstad, SWEDEN</p>
    <p class="foot-line" style="margin-top:12px; display:flex; align-items:center; gap:12px;"><svg width="14" height="11" viewBox="0 0 14 11"><rect x="0.5" y="0.5" width="13" height="10" fill="#b5b5b5"/><path d="M1 1 L7 6 L13 1" fill="none" stroke="#111" stroke-width="1.3"/></svg>info@companyname.com</p>
  </div>

  <div class="abs col-hours">
    <div class="foot-head">Hours</div>
    <p class="foot-line" style="margin-top:14px;">Mon–Fri: 9:00AM–5:00PM</p>
    <p class="foot-line hours-row" style="margin-top:12px;"><span>Sat &amp; Sun:</span><span>11:00AM–3:00PM</span></p>
  </div>

  <div class="abs col-email">
    <div class="foot-head">Email Sign Up</div>
    <div class="signup">
      <div class="signup-field">Enter Email Address</div>
      <div class="signup-btn"><svg width="10" height="14" viewBox="0 0 10 14"><path d="M2 1 L8 7 L2 13" fill="none" stroke="#fff" stroke-width="2.5"/></svg></div>
    </div>
  </div>

</div>
</body>
</html>
```